Sports Card - Swimming

I have a project to design sports cards for college athletes of sports not so recognize by the media. Starting with swimming.
I always admire the design of the Glintra collection from Torvello, in the attached file you can see some examples of this collection.
The idea of this project is to be non-profit, just to celebrate the achievements of these athletes, and maybe in the future provide them some copies of these cards.

I need editable templates on Photoshop of these cards, so I can personalize them for multiple athletes, and universities colors. The choose designer(s) will be contact in the future for more projects, starting with the back of the cards. Sports card are 2.5in x 3.5in, and that's the only fix requirement I have.

```html
<!DOCTYPE html>
<html lang="en">
<head>
<meta charset="utf-8">
<title>Swimming Sports Card</title>
<link href="https://fonts.googleapis.com/css2?family=Kalam:wght@700&display=swap" rel="stylesheet">
<style>
  :root {
    --page: #ffffff;
    --deep-red: #b00d0d;
    --coral: #f5405a;
    --amber: #f99d24;
    --panel: #ffffff;
    --ink: #111111;
    --water-light: #a6e4ec;
    --water-mid: #6ccbd9;
    --water-deep: #4bb6c8;
  }
  html, body {
    margin: 0;
    padding: 0;
    width: 927px;
    height: 1200px;
    overflow: hidden;
    background: var(--page);
  }
  .canvas {
    position: relative;
    width: 927px;
    height: 1200px;
  }
  .sports-card {
    position: absolute;
    left: 204px;
    top: 236px;
    width: 518px;
    height: 726px;
    filter: drop-shadow(3px 4px 4px rgba(0,0,0,0.35));
  }
  .sports-card svg {
    display: block;
    width: 100%;
    height: 100%;
  }
  .deep-red { fill: var(--deep-red); }
  .coral { fill: var(--coral); }
  .amber { fill: var(--amber); }
  .panel { fill: var(--panel); }
  .signature-label {
    font-family: "Kalam", cursive;
    font-weight: 700;
    font-size: 40px;
    fill: var(--ink);
  }
</style>
</head>
<body>
<main class="canvas">
  <article class="sports-card">
    <svg viewBox="0 0 475 666" xmlns="http://www.w3.org/2000/svg">
      <defs>
        <linearGradient id="water" x1="0" y1="0" x2="0" y2="1">
          <stop offset="0" stop-color="var(--water-light)"/>
          <stop offset="0.55" stop-color="var(--water-mid)"/>
          <stop offset="1" stop-color="var(--water-deep)"/>
        </linearGradient>
        <filter id="edge-shadow" x="-5%" y="-5%" width="110%" height="110%">
          <feDropShadow dx="0" dy="2" stdDeviation="2" flood-color="#000" flood-opacity="0.3"/>
        </filter>
      </defs>

      <!-- card base -->
      <rect class="deep-red" x="0" y="0" width="475" height="666"/>

      <!-- top bands -->
      <g class="top-bands" filter="url(#edge-shadow)">
        <polygon class="amber" points="0,22 475,70 475,150 395,158 88,66 0,150"/>
        <polygon class="coral" points="0,0 60,0 475,62 475,92 0,20"/>
      </g>

      <!-- left side strip -->
      <polygon class="amber" points="0,150 40,150 30,260 22,330 30,420 0,460"/>
      <polygon class="deep-red" points="0,190 18,190 28,300 14,400 22,470 0,470"/>

      <!-- photo area -->
      <polygon class="athlete-photo" role="img" aria-label="Action photo of a swimmer breathing mid freestyle stroke in a pool, lane rope behind"
               fill="url(#water)" filter="url(#edge-shadow)"
               points="38,68 395,152 470,150 470,470 8,505 8,190"/>

      <!-- right accent -->
      <polygon class="coral" points="400,205 475,150 475,205"/>
      <polygon class="amber" points="462,220 475,215 475,440 462,360 470,300"/>

      <!-- left lower accent -->
      <polygon class="coral" points="0,458 55,530 0,560"/>

      <!-- bottom bands -->
      <g class="bottom-bands">
        <polygon class="amber" points="0,580 150,590 400,660 475,600 475,666 0,666"/>
        <polygon class="coral" points="0,640 95,618 330,666 0,666"/>
        <polygon class="deep-red" points="0,656 85,634 230,666 0,666"/>
      </g>

      <!-- signature panel -->
      <polygon class="panel" filter="url(#edge-shadow)"
               points="8,504 475,476 475,600 400,655 150,588 0,584 0,560 55,530"/>
      <polygon class="coral" points="432,500 475,492 475,540"/>

      <text class="signature-label" x="290" y="562" text-anchor="middle" transform="rotate(-9 290 548)">Signature</text>
    </svg>
  </article>
</main>
</body>
</html>
```